Velmorra Aviation - Insurance Brokers - Half page magazine ad.

Half-page ad in an aviation industry magazine promoting our services as an aviation insurance broker. I've attached an example of a pop-up banner we used at a conference recently to give you an idea.

I have attached a copy of the specifications from the publisher. Half-page ad requires:
- 190mm width x 132mm height
- Minimum 300 dpi
- colours in CMYK
- high resolution PDF with fonts embedded

Target Market(s)

Aircraft owners/operators, drone owners/operators, pilots

Font styles to use
Serif

Colors

Designer to choose colors to be used in the design.

Requirements
Must have
• 1. Company logo (attached).
• 2. Contact Details as follows:
• www.qtnaviation.com.au
• (02) 4193 7625
Nice to have
• Maybe a picture of an aircraft/helicopter in the bakground with logo/text etc over the top. But happy to look at alternative design options.

```html
<!DOCTYPE html>
<html lang="en">
<head>
<meta charset="utf-8">
<title>Velmorra Aviation – Specialist Insurance Aviation Broker</title>
<link href="https://fonts.googleapis.com/css2?family=Playfair+Display:wght@700;800;900&family=Lora:wght@400;600;700&display=swap" rel="stylesheet">
<style>
  :root{
    --backdrop:#e9ebed;
    --page:#ffffff;
    --navy-deep:#0b1830;
    --navy:#1d3a6b;
    --sky:#5a82b0;
    --haze:#9fb6cf;
    --flare:#d06a28;
    --accent-red:#e0143c;
    --brand-blue:#1c3f8f;
    --ink:#3a3d42;
    --muted:#f1f2f3;
  }
  *{box-sizing:border-box;margin:0;padding:0}
  html,body{width:1200px;height:1200px;overflow:hidden}
  body{background:var(--backdrop);display:flex;align-items:center;justify-content:center;font-family:"Lora",serif;color:var(--ink)}

  .ad-page{width:1100px;height:764px;background:var(--page);box-shadow:0 6px 24px rgba(0,0,0,.15);display:flex;flex-direction:column;overflow:hidden}

  .hero{position:relative;height:300px;overflow:hidden;color:#fff;flex:none}
  .hero-sky{position:absolute;inset:0;background:
      radial-gradient(ellipse 35% 40% at 58% 100%,var(--flare) 0%,rgba(208,106,40,0) 70%),
      radial-gradient(ellipse 60% 70% at 55% 45%,var(--sky) 0%,rgba(90,130,176,0) 70%),
      linear-gradient(160deg,var(--navy-deep) 0%,var(--navy) 55%,var(--navy-deep) 100%)}
  .hero-aircraft{position:absolute;left:380px;top:120px;width:460px;height:150px;border-radius:50%;
      background:radial-gradient(ellipse at center,rgba(220,230,242,.85) 0%,rgba(159,182,207,.45) 45%,rgba(159,182,207,0) 72%)}
  .hero-insets{position:absolute;right:150px;bottom:18px;display:flex;gap:8px}
  .hero-inset{width:78px;height:52px;border:2px solid #fff;background:linear-gradient(135deg,#c9d6e3,#5d7fa3)}

  .hero-title{position:absolute;top:28px;right:44px;text-align:right;font-family:"Playfair Display",serif;font-weight:900;line-height:1}
  .hero-kicker{color:var(--accent-red);font-size:40px;letter-spacing:3px}
  .hero-headline{font-size:58px;letter-spacing:3px;margin-top:8px}

  .service-lists{position:absolute;left:44px;bottom:26px;display:flex;gap:48px;font-family:"Lora",serif;font-weight:700;font-size:16px}
  .service-lists ul{list-style:none}
  .service-lists li{margin-top:5px}
  .service-lists li::before{content:"";display:inline-block;width:7px;height:7px;border-radius:50%;background:#fff;margin-right:10px;vertical-align:middle}
  .service-lists .secondary{padding-top:26px}

  .brand-bar{flex:none;height:80px;display:flex;align-items:center;justify-content:space-between;padding:0 44px;border-bottom:1px solid #e2e4e7}
  .brand-name{display:flex;align-items:center;gap:12px;font-family:"Playfair Display",serif;font-weight:800;font-size:30px;color:var(--brand-blue)}
  .brand-mark{width:26px;height:26px;background:var(--brand-blue)}
  .contact{font-family:"Lora",serif;font-weight:700;color:var(--brand-blue);font-size:18px;text-align:right}
  .contact-line{display:flex;align-items:center;justify-content:flex-end;gap:8px;margin:3px 0}
  .contact svg{width:18px;height:18px}

  .content{flex:1;min-height:0;display:flex;gap:30px;padding:24px 44px 26px;background:var(--muted)}
  .gallery{width:230px;display:flex;flex-direction:column;gap:8px;flex:none}
  .gallery-photo{flex:1}
  .photo-snow{background:linear-gradient(135deg,#eef3f7,#b9cad8)}
  .photo-city{background:linear-gradient(180deg,#2f6f86,#173a4c 70%,#d8a04a)}
  .photo-interior{background:linear-gradient(135deg,#f4f7fa,#9db3c8)}

  .article{flex:1;min-width:0;overflow:hidden}
  .article h2{font-family:"Playfair Display",serif;font-weight:700;font-size:30px;line-height:1.05;color:#2b2e33;margin-bottom:12px}
  .article-columns{column-count:2;column-gap:28px;font-size:12px;line-height:1.5;text-align:justify}
  .article-columns p{margin-bottom:9px}
</style>
</head>
<body>
<main class="ad-page">
  <section class="hero">
    <div class="hero-sky" role="img" aria-label="Dramatic blue sky with a warm sunset glow behind the aircraft"></div>
    <div class="hero-aircraft" role="img" aria-label="Passenger jet on approach with landing gear down"></div>
    <div class="hero-insets">
      <div class="hero-inset" role="img" aria-label="Helicopter photo"></div>
      <div class="hero-inset" role="img" aria-label="Drone photo"></div>
      <div class="hero-inset" role="img" aria-label="Light aircraft photo"></div>
    </div>
    <div class="hero-title">
      <div class="hero-kicker">SPECIALIST INSURANCE</div>
      <div class="hero-headline">AVIATION BROKER</div>
    </div>
    <div class="service-lists">
      <ul>
        <li>Rotorwing</li>
        <li>Fixed wing</li>
        <li>Manufacturas</li>
        <li>Loss of licence</li>
      </ul>
      <ul class="secondary">
        <li>MRO's</li>
        <li>Drones</li>
        <li>Personal Accident</li>
      </ul>
    </div>
  </section>

  <section class="brand-bar">
    <div class="brand-name"><span class="brand-mark"></span>Velmorra Aviation</div>
    <div class="contact">
      <div class="contact-line">
        <svg viewBox="0 0 24 24" aria-hidden="true"><path fill="#e0143c" d="M6.6 10.8a15.1 15.1 0 0 0 6.6 6.6l2.2-2.2a1 1 0 0 1 1-.25 11.4 11.4 0 0 0 3.6.57 1 1 0 0 1 1 1V20a1 1 0 0 1-1 1A17 17 0 0 1 3 4a1 1 0 0 1 1-1h3.5a1 1 0 0 1 1 1c0 1.25.2 2.45.57 3.6a1 1 0 0 1-.25 1z"/></svg>
        (02) 4193 7625
      </div>
      <div class="contact-line">
        <svg viewBox="0 0 24 24" aria-hidden="true"><circle cx="12" cy="12" r="10" fill="#e0143c"/><path d="M2 12h20M12 2c3 3 3 17 0 20M12 2c-3 3-3 17 0 20" stroke="#fff" stroke-width="1.4" fill="none"/></svg>
        www.qtnaviation.com.au
      </div>
    </div>
  </section>

  <section class="content">
    <div class="gallery">
      <div class="gallery-photo photo-snow" role="img" aria-label="Snow-covered winter landscape"></div>
      <div class="gallery-photo photo-city" role="img" aria-label="City waterfront skyline at dusk"></div>
      <div class="gallery-photo photo-interior" role="img" aria-label="Bright modern glass building interior"></div>
    </div>
    <article class="article">
      <h2>Professional Designs</h2>
      <div class="article-columns">
        <p>Lorem ipsum dolor sit amet, consectetur adipisicing elit, sed do eiusmod tempor incididunt ut labore et dolore magna aliqua. Ut enim ad minim veniam, quis nostrud.</p>
        <p>Exercitation ullamco laboris nisi ut aliquip ex ea commodo consequat. Duis aute irure dolor in reprehenderit in voluptate velit esse cillum dolore eu fugiat nulla pariatur mollit anim id est laborum.</p>
        <p>Duis aute irure dolor in reprehenderit in voluptate velit esse cillum dolore eu fugiat nulla pariatur. Excepteur sint occaecat cupidatat non proident, veniam quis nostrud.</p>
        <p>Dolor in reprehenderit in voluptate velit esse cillum dolore eu fugiat nulla pariatur. Duis aute irure dolor in reprehenderit in voluptate velit esse cillum dolore eu fugiat.</p>
        <p>Nulla pariatur. Duis aute irure dolor in reprehenderit in voluptate velit esse cillum dolore eu fugiat nulla pariatur. Excepteur sint occaecat cupidatat non proident.</p>
        <p>Duis aute irure dolor in reprehenderit in voluptate velit esse cillum dolore eu fugiat nulla pariatur. Lorem ipsum dolor sit amet, consectetur adipisicing elit, sed do eiusmod tempor.</p>
      </div>
    </article>
  </section>
</main>
</body>
</html>
```